I need to redesign this website. Modern Fun Professional Redesign For www.JollyPerkHub.com = New Name www.ClaimVouchly.com

Use existing content as it is on website exactly and we will revise after initial mock ups.

The new name will be ClaimVouchly.com please make a quick logo for this site too while redesigning.

Make it look like an official website....

Target Market(s)

Consumers that are redeeming certificates that businesses gave to them as a gift for customer loyalty,e tc.

Industry/Entity Type

It Professional

Logo Text

www.ClaimVouchly.com

Number of Pages Required

4 page

Colors

Designer to choose colors to be used in the design.

Requirements
Must have
• Must look professional, build trust and credibility.
Nice to have
• open
Should not have
• open

```html
<!DOCTYPE html>
<html lang="en">
<head>
<meta charset="utf-8">
<title>ClaimVouchly.com</title>
<link href="https://fonts.googleapis.com/css2?family=Roboto:wght@400;500;700&family=Lato:wght@700&family=Open+Sans:wght@300;400&display=swap" rel="stylesheet">
<style>
:root{
  --brand:#ff4512;
  --brand-deep:#f2420f;
  --ink:#4a4a4a;
  --ink-soft:#6b6b6b;
  --line:#d9d9d9;
  --white:#ffffff;
  --dark:#333333;
}
*{box-sizing:border-box;margin:0;padding:0}
html,body{width:1093px;height:1200px;overflow:hidden;background:var(--white)}
body{font-family:"Open Sans",sans-serif;color:var(--ink);position:relative}
.container{width:771px;margin:0 auto;position:relative}

.site-header{height:58px;background:var(--white)}
.site-header .container{display:flex;align-items:center;height:58px}
.brand{display:flex;align-items:center;gap:8px;font-family:"Roboto",sans-serif;font-weight:500;font-size:22px;color:var(--brand);letter-spacing:.2px}
.brand-dot{width:26px;height:26px;border-radius:50%;background:var(--brand)}
.main-nav{margin-left:auto;display:flex;gap:20px;font-family:"Roboto",sans-serif;font-size:13px;color:var(--dark)}
.header-icons{display:flex;gap:6px;margin-left:34px;align-items:center}
.header-icons svg{display:block}

.hero{position:relative;height:497px;overflow:hidden}
.hero-photo{position:absolute;inset:0;background:linear-gradient(120deg,#6d5a4e 0%,#8a7d74 30%,#9a8f88 50%,#6b6460 75%,#4d4a4a 100%)}
.hero-shade{position:absolute;inset:0;background:rgba(0,0,0,.18)}
.hero-content{position:absolute;left:0;right:0;top:240px;text-align:center;color:var(--white);font-family:"Roboto",sans-serif}
.hero-title{font-size:39px;font-weight:700;letter-spacing:-.5px;line-height:1}
.hero-sub{font-size:17px;font-weight:700;margin-top:8px;letter-spacing:-.2px}
.redeem-form{width:683px;height:67px;margin:9px auto 0;background:rgba(0,0,0,.55);border-radius:5px;display:flex;align-items:center;padding:0 10px;gap:11px}
.redeem-input{flex:0 0 502px;height:49px;background:var(--white);border-radius:6px;display:flex;align-items:center;padding-left:15px;font-size:13px;color:#6a6a6a}
.redeem-submit{flex:1;height:48px;background:var(--brand);border-radius:5px;display:flex;align-items:center;justify-content:center;font-size:16px;font-weight:700;color:var(--white)}

.how-it-works{height:158px;text-align:center;padding-top:28px}
.section-title{font-family:"Lato",sans-serif;font-weight:700;font-size:29px;color:#555;letter-spacing:-.3px}
.section-title span{color:var(--brand)}
.how-it-works p{width:720px;margin:16px auto 0;font-size:13px;line-height:19px;color:var(--ink-soft)}

.testimonials{position:relative;height:245px;overflow:hidden;text-align:center;color:var(--white)}
.testimonials-photo{position:absolute;inset:0;background:linear-gradient(90deg,#ff4a17 0%,#ff5a2a 45%,#ff4f1d 70%,#ff4712 100%)}
.testimonials-inner{position:relative;padding-top:40px}
.testimonials .section-title{color:var(--white);font-size:27px}
.quote{font-size:13px;line-height:19px;margin-top:14px}
.author{font-size:17px;margin-top:20px}
.meta{font-size:10.5px;line-height:13px;margin-top:3px}
.arrow{position:absolute;top:105px}
.arrow.prev{left:140px}
.arrow.next{left:928px}

.site-footer{padding-top:41px}
.footer-cols{display:flex;height:145px}
.footer-col h4{font-family:"Roboto",sans-serif;font-weight:400;font-size:15.5px;color:var(--ink);margin-bottom:14px}
.footer-col a{display:block;font-size:12px;line-height:24px;color:var(--ink-soft);text-decoration:none}
.col-company{width:177px}
.col-support{width:219px}
.col-legal{width:199px}
.social{display:flex;gap:6px;margin-left:-6px}
.social span{width:37px;height:37px;border-radius:50%;border:1px solid #e3e3e3;display:block}
.cards{display:flex;gap:6px;margin-top:10px;margin-left:-3px}
.cards span{width:40px;height:25px;border-radius:2px;display:block}
.cards span:nth-child(1){background:#1d2f6f}
.cards span:nth-child(2){background:#e8e8e8}
.cards span:nth-child(3){background:#2b7fc2}
.cards span:nth-child(4){background:#f0f0f0}
.footer-rule{width:998px;margin:0 auto;border-top:1px solid var(--line)}
.copyright{text-align:center;font-size:12px;color:#8a8a8a;padding-top:14px}
.bottom-bar{position:absolute;left:0;right:0;bottom:0;height:10px;background:var(--dark)}
</style>
</head>
<body>

<header class="site-header">
  <div class="container">
    <div class="brand"><span class="brand-dot"></span>ClaimVouchly</div>
    <nav class="main-nav">
      <span>Home</span><span>Contact Us</span><span>Testimonials</span><span>Terms</span>
    </nav>
    <div class="header-icons">
      <svg width="15" height="13" viewBox="0 0 15 13"><path d="M7.5 1 L1 6.5 H3 V12 H6 V8.5 H9 V12 H12 V6.5 H14 Z" fill="#666"/></svg>
      <svg width="13" height="13" viewBox="0 0 13 13"><rect x=".5" y=".5" width="12" height="12" rx="2" fill="#666"/></svg>
      <svg width="16" height="13" viewBox="0 0 16 13"><rect x="1" y="1.5" width="14" height="10" rx="1.5" fill="none" stroke="#666" stroke-width="1.4"/><path d="M1.5 2.5 L8 7.5 L14.5 2.5" fill="none" stroke="#666" stroke-width="1.4"/></svg>
    </div>
  </div>
</header>

<section class="hero">
  <div class="hero-photo" role="img" aria-label="Photo of three colleagues reviewing documents together at a desk"></div>
  <div class="hero-shade"></div>
  <div class="hero-content">
    <h1 class="hero-title">WELCOME TO THE CLAIMVOUCHLY</h1>
    <p class="hero-sub">PLEASE ENTER A VALID CERTIFICATE ID IN THE FORM BELOW</p>
    <div class="redeem-form">
      <div class="redeem-input">Enter Your Redeem Certification</div>
      <div class="redeem-submit">SUBMIT NOW</div>
    </div>
  </div>
</section>

<section class="how-it-works">
  <h2 class="section-title">HOW IT <span>WORKS</span></h2>
  <p>JollyPerkHub.com is a leading company in travel certificate fulfillment. Our goal is to make it easy for you to redeem your certificate and our philosophy is this: "What good is it to receive a gift certificate if you can't use it?". If you have any questions about how to redeem a certain certificate, please contact us. We are here to help.</p>
</section>

<section class="testimonials">
  <div class="testimonials-photo" role="img" aria-label="Orange-tinted photo of a smiling couple"></div>
  <svg class="arrow prev" width="16" height="28" viewBox="0 0 16 28"><path d="M14 2 L2 14 L14 26" fill="none" stroke="#fff" stroke-width="2"/></svg>
  <svg class="arrow next" width="16" height="28" viewBox="0 0 16 28"><path d="M2 2 L14 14 L2 26" fill="none" stroke="#fff" stroke-width="2"/></svg>
  <div class="testimonials-inner">
    <h2 class="section-title">TESTIMONIALS</h2>
    <p class="quote">"Marla was a "saving grace.' She followed up and helped me book the vacation and air fare.<br>Marla was positive and did everything she promised to do. "</p>
    <p class="author">Dana R.</p>
    <p class="meta">Dayton, OH<br>Added on 06/23/2017 06:24:16 pm</p>
  </div>
</section>

<footer class="site-footer">
  <div class="container footer-cols">
    <div class="footer-col col-company">
      <h4>Company Based</h4>
      <a>About us</a><a>News</a><a>Career Opportunities</a>
    </div>
    <div class="footer-col col-support">
      <h4>Support and Notification</h4>
      <a>Frequently Asked Questions</a><a>Contact us</a><a>Our dealers</a>
    </div>
    <div class="footer-col col-legal">
      <h4>Legal</h4>
      <a>Terms of use</a><a>Privacy policy &amp; Service Policy</a><a>Sitemap</a>
    </div>
    <div class="footer-col col-follow">
      <h4>Follow us</h4>
      <div class="social"><span></span><span></span><span></span><span></span></div>
      <div class="cards"><span></span><span></span><span></span><span></span></div>
    </div>
  </div>
  <div class="footer-rule"></div>
  <p class="copyright">2017 all rights reserved.</p>
</footer>
<div class="bottom-bar"></div>

</body>
</html>
```